Custom Home Builder Brochure
Marcus Hollery Construction LLC
Custom Home Builder Brochure - Construction
Creative Brief
Construction
Potential clients for building a new, custom home.
- Calm colors, nothing too bold - Easy to read font - Use the slogan "You Dream It. We'll Build It." with the font that is close to or matches our logo - Include all text that was given in the "details" section of this form.
marcushollerybuilds marcushollerybuilds
I am not sure what a vector file is, please advise. Thank you.
MegaPixelNomad MegaPixelNomad
Dear Project holder, I would be pleased if you could send me the vector file of your logo. Thanks

```html
<!DOCTYPE html>
<html lang="en">
<head>
<meta charset="utf-8">
<title>Marcus Hollery Construction — Custom Home Brochure</title>
<link href="https://fonts.googleapis.com/css2?family=Marcellus&family=Lato:wght@400;700&display=swap" rel="stylesheet">
<style>
  :root {
    --paper: #efe6d5;
    --paper-deep: #e4d6bd;
    --orange: #d8762b;
    --rust: #b85a1e;
    --brown: #5b3a24;
    --ink: #3a2a1d;
    --frame: #fbf7ef;
  }
  * { margin: 0; padding: 0; box-sizing: border-box; }
  html, body { width: 1200px; height: 778px; overflow: hidden; background: var(--paper); }
  .spread {
    position: relative; width: 1200px; height: 778px; overflow: hidden;
    background: linear-gradient(90deg, var(--paper) 0%, var(--paper-deep) 33.4%, var(--paper) 33.6%, var(--paper-deep) 66.8%, var(--paper) 67%, var(--paper-deep) 100%);
    font-family: "Lato", sans-serif; color: var(--ink);
  }
  .swooshes { position: absolute; inset: 0; }
  .copy { position: absolute; font-size: 10.5px; line-height: 1.42; text-align: justify; }
  .copy--narrow { font-size: 9.5px; line-height: 1.4; text-align: left; }
  .copy .dropcap { float: left; font-family: "Marcellus", serif; font-size: 40px; line-height: 32px; margin-right: 4px; color: var(--brown); }
  .heading {
    position: absolute; font-family: "Marcellus", serif; font-size: 25px; font-weight: 400; color: var(--orange);
    display: flex; align-items: center; gap: 8px; white-space: nowrap; line-height: 1;
  }
  .heading .mark { width: 14px; height: 14px; background: var(--orange); border-radius: 50%; flex: none; }
  .slogan {
    position: absolute; font-family: "Marcellus", serif; font-size: 22px; color: var(--brown);
    white-space: nowrap; line-height: 1; text-align: center;
  }
  .photo {
    position: absolute; border: 4px solid var(--frame);
    box-shadow: 0 2px 5px rgba(60, 40, 20, .35);
  }
  .photo--wood { background: linear-gradient(160deg, #8a5a34, #5e3a20 60%, #c9a27a); }
  .photo--kitchen { background: linear-gradient(170deg, #d9c7a8, #8b6540 55%, #3e2a1a); }
  .photo--stone { background: linear-gradient(180deg, #b8a48a, #7c6a55 50%, #4a3a2c); }
  .photo--exterior { background: linear-gradient(180deg, #9fb6c9 0%, #a59478 45%, #5d6b3e 100%); }
  .photo--patio { background: linear-gradient(180deg, #c7b08c, #7b5838 60%, #6f7a45); }
</style>
</head>
<body>
<main class="spread">

  <svg class="swooshes" width="1200" height="778" viewBox="0 0 1200 778" aria-hidden="true">
    <path d="M0 150 C120 172 260 142 400 160 L400 184 C260 170 120 204 0 178 Z" fill="var(--orange)"/>
    <path d="M100 196 C200 186 320 192 400 204 L400 216 C320 206 200 202 100 212 Z" fill="var(--brown)"/>
    <path d="M0 490 C120 470 260 500 400 480 L400 500 C260 522 120 494 0 516 Z" fill="var(--orange)"/>
    <path d="M408 130 C540 150 680 120 804 140 L804 156 C680 138 540 168 408 148 Z" fill="var(--orange)"/>
    <path d="M408 372 C540 392 680 360 804 378 L804 392 C680 376 540 408 408 388 Z" fill="var(--rust)"/>
    <path d="M804 440 C940 470 1080 420 1200 450 L1200 474 C1080 446 940 496 804 466 Z" fill="var(--orange)"/>
    <path d="M804 512 C940 534 1080 506 1200 522 L1200 534 C1080 520 940 548 804 526 Z" fill="var(--brown)"/>
  </svg>

  <!-- Left panel -->
  <p class="copy" style="left:14px; top:12px; width:382px;">
    <span class="dropcap">I</span>t is often said that anything worth doing is worth doing right. At Marcus Hollery Construction, we build each home as if it were our own. Building a house is more than just raising walls; it is creating a place where your family will grow and gather for years to come. We work closely with you from the first sketch to the final walkthrough, and we stand behind every home we build. We want to make your dream come true.
  </p>

  <h2 class="heading" style="left:112px; top:226px;"><span class="mark"></span>An Honest Builder</h2>

  <div class="photo photo--kitchen" style="left:118px; top:262px; width:176px; height:160px;" role="img" aria-label="Photo of a finished kitchen with wood cabinets"></div>

  <p class="copy copy--narrow" style="left:302px; top:262px; width:94px;">
    Marcus Hollery Construction is a small, independent business built on the passion of Marcus Hollery. For almost 20 years he has built custom homes across the region. He takes the time to know you and your family and is involved in every project. His word is his bond.
  </p>

  <h2 class="heading" style="left:40px; top:528px;"><span class="mark"></span>Quality Construction</h2>

  <p class="copy" style="left:40px; top:562px; width:356px;">
    When you trust us to build your home, you can expect quality construction from the ground up. Every phase is carefully planned and managed by our own team, using the finest materials available. We never take shortcuts, so every detail is done right.
  </p>

  <div class="photo photo--exterior" style="left:30px; top:630px; width:252px; height:140px;" role="img" aria-label="Photo of a brick house with a covered front porch"></div>

  <p class="copy copy--narrow" style="left:292px; top:630px; width:104px;">
    From the rebuilding of the foundation to the final trim, Marcus treats each home as if he were building it for his own family. He checks every step and takes pride in work that lasts for generations.
  </p>

  <!-- Middle panel -->
  <h2 class="heading" style="left:430px; top:20px;"><span class="mark"></span>Attention To Detail</h2>

  <p class="copy" style="left:420px; top:52px; width:372px;">
    When you dream about your ideal home, you can imagine every last detail. We pay attention to every one of them. From the stone on the fireplace to the trim in the hallway and the hardware on the cabinets, we make sure it is exactly how you pictured it. We listen to your ideas and bring them to life.
  </p>

  <div class="photo photo--kitchen" style="left:420px; top:168px; width:156px; height:158px;" role="img" aria-label="Photo of a kitchen island with pendant lights"></div>
  <div class="photo photo--wood" style="left:584px; top:162px; width:212px; height:166px;" role="img" aria-label="Photo of a covered wooden outdoor pavilion"></div>

  <div class="photo photo--stone" style="left:412px; top:402px; width:176px; height:154px;" role="img" aria-label="Photo of a living room with a stone fireplace"></div>
  <div class="photo photo--wood" style="left:596px; top:396px; width:200px; height:144px;" role="img" aria-label="Photo of a great room with exposed wood beams"></div>
  <div class="photo photo--patio" style="left:420px; top:566px; width:166px; height:200px;" role="img" aria-label="Photo of a stone outdoor kitchen"></div>
  <div class="photo photo--kitchen" style="left:596px; top:552px; width:204px; height:214px;" role="img" aria-label="Photo of a dining area with wood ceiling"></div>

  <!-- Right panel -->
  <div class="photo photo--stone" style="left:812px; top:12px; width:180px; height:196px;" role="img" aria-label="Photo of a tall stone fireplace"></div>
  <div class="photo photo--kitchen" style="left:1000px; top:12px; width:188px; height:140px;" role="img" aria-label="Photo of a bright kitchen"></div>
  <div class="photo photo--patio" style="left:1000px; top:160px; width:188px; height:120px;" role="img" aria-label="Photo of a covered patio"></div>
  <div class="photo photo--wood" style="left:812px; top:216px; width:180px; height:210px;" role="img" aria-label="Photo of a wood paneled room"></div>
  <div class="photo photo--exterior" style="left:1000px; top:290px; width:188px; height:140px;" role="img" aria-label="Photo of a house exterior with garden"></div>

  <p class="slogan" style="left:804px; top:484px; width:396px;">You Dream It. We'll Build It.</p>

  <h2 class="heading" style="left:850px; top:544px;"><span class="mark"></span>Customer Service</h2>

  <p class="copy" style="left:812px; top:578px; width:378px;">
    When Marcus Hollery Construction builds your home, you don't have to wonder what is going on or who to call. Marcus is with you for the most important part of the process. He maintains close contact with you and your family, informing you on progress and listening to your thoughts and ideas. Marcus wants to make sure the home he builds meets your expectations. We value the trust you place in us and we work to earn it every day. We will schedule meetings with you and keep you involved so you can enjoy the making of your dream home.
  </p>

</main>
</body>
</html>
```